Garlic Farm for Farm Sales/Restaurant sales

Need a professional, but appealing to agriculture world. We are selling 27 kinds of Organic Garlic from a farm in Simla,CO. I have uploaded logo and business information-we are going to need a template, because I will need to use it for four separate people.
-We are trying to appeal to Farm to table restaurants
-As well as growers/farmers

Target Market(s)

Agriculture Sales/Restaurants-Organic

Industry/Entity Type

Agriculture

Contact Information for Business Card

Want it to look more unique then your average orbel mart card- I want it to look amazing

Font styles to use
Sans Serif

Colors
0455a3
ec1f27
fbed22
ffffff

Requirements
Must have
• Just be creative
Nice to have
• Colorful
Should not have
• plain

```html
<!DOCTYPE html>
<html lang="en">
<head>
<meta charset="utf-8">
<title>Ridgeline Garlic Co — Business Card</title>
<link rel="stylesheet" href="https://fonts.googleapis.com/css2?family=Montserrat:wght@500;600;700;800&display=swap">
<style>
  :root{
    --stage:#1f1f21;
    --red:#c8202f;
    --plum:#4b2f5f;
    --crimson:#a41f3b;
    --coral:#d1564a;
    --navy:#1c2f63;
    --yellow:#fbd422;
    --white:#ffffff;
  }
  *{box-sizing:border-box;margin:0;padding:0}
  html,body{width:1200px;height:873px;overflow:hidden;background:var(--stage);font-family:"Montserrat",sans-serif}
  .stage{position:relative;width:1200px;height:873px}
  .card{position:absolute;width:620px;height:354px;border-radius:22px;overflow:hidden;box-shadow:0 18px 40px rgba(0,0,0,.55)}

  /* front */
  .card--front{left:110px;top:66px;display:flex;flex-direction:column}
  .band{width:100%}
  .band--red{height:22%;background:var(--red)}
  .band--plum{height:22%;background:var(--plum)}
  .band--crimson{height:22%;background:var(--crimson)}
  .band--coral{flex:1;background:var(--coral)}
  .front-mark{position:absolute;inset:0;display:flex;align-items:center;justify-content:center;gap:16px}
  .mark-dot{width:46px;height:46px;border-radius:50%;background:var(--yellow)}
  .front-name{color:var(--white);font-weight:800;font-size:34px;letter-spacing:.5px}

  /* back */
  .card--back{left:470px;top:452px;background:var(--white)}
  .back-shapes{position:absolute;inset:0}
  .brand{position:absolute;left:40px;top:92px;display:flex;align-items:center;gap:12px}
  .brand-dot{width:38px;height:38px;border-radius:50%;background:var(--red)}
  .brand-name{color:var(--navy);font-weight:800;font-size:26px;line-height:1.05}
  .social{position:absolute;left:92px;top:178px;display:flex;gap:12px}
  .social span{width:22px;height:22px;border-radius:50%;background:var(--navy)}
  .social span:nth-child(2){background:var(--red)}
  .social span:nth-child(3){background:var(--yellow)}
  .contact{position:absolute;right:30px;top:142px;text-align:right;color:var(--white)}
  .contact-name{font-weight:700;font-size:19px;letter-spacing:.5px;margin-bottom:4px;padding-right:22px}
  .contact-line{display:flex;justify-content:flex-end;align-items:center;gap:8px;font-weight:500;font-size:13px;line-height:21px}
  .contact-line svg{width:14px;height:14px;fill:var(--yellow);flex:none}
</style>
</head>
<body>
<main class="stage">

  <section class="card card--front" aria-label="Card front">
    <div class="band band--red"></div>
    <div class="band band--plum"></div>
    <div class="band band--crimson"></div>
    <div class="band band--coral"></div>
    <div class="front-mark">
      <span class="mark-dot"></span>
      <span class="front-name">Ridgeline Garlic Co</span>
    </div>
  </section>

  <section class="card card--back" aria-label="Card back">
    <svg class="back-shapes" viewBox="0 0 620 354" width="620" height="354" aria-hidden="true">
      <path d="M545 0 C470 110 300 220 0 300 L0 354 L620 354 L620 0 Z" fill="var(--red)"/>
      <path d="M535 0 C460 106 290 214 0 292" fill="none" stroke="var(--yellow)" stroke-width="5"/>
      <path d="M444 72 C380 170 260 240 0 284" fill="none" stroke="var(--navy)" stroke-width="7"/>
    </svg>

    <div class="brand">
      <span class="brand-dot"></span>
      <span class="brand-name">Ridgeline<br>Garlic Co</span>
    </div>
    <div class="social" aria-label="Social channels">
      <span></span><span></span><span></span><span></span>
    </div>

    <div class="contact">
      <p class="contact-name">DANA WHITFIELD</p>
      <p class="contact-line">555-014-2290
        <svg viewBox="0 0 24 24"><path d="M6.6 10.8a15 15 0 0 0 6.6 6.6l2.2-2.2a1 1 0 0 1 1-.25 11.4 11.4 0 0 0 3.6.57 1 1 0 0 1 1 1V20a1 1 0 0 1-1 1A17 17 0 0 1 3 4a1 1 0 0 1 1-1h3.5a1 1 0 0 1 1 1c0 1.25.2 2.45.57 3.57a1 1 0 0 1-.25 1z"/></svg></p>
      <p class="contact-line">dana@ridgelinegarlic.com
        <svg viewBox="0 0 24 24"><path d="M2 5h20v14H2z M3 6l9 7 9-7" fill="var(--yellow)" stroke="var(--red)" stroke-width="1.5"/></svg></p>
      <p class="contact-line">www.ridgelinegarlic.com
        <svg viewBox="0 0 24 24"><circle cx="12" cy="12" r="10"/><path d="M2 12h20M12 2c3 3 3 17 0 20M12 2c-3 3-3 17 0 20" fill="none" stroke="var(--red)" stroke-width="1.5"/></svg></p>
      <p class="contact-line">P.O. Box 12 Elmwood, CO 80000
        <svg viewBox="0 0 24 24"><path d="M12 2a7 7 0 0 0-7 7c0 5 7 13 7 13s7-8 7-13a7 7 0 0 0-7-7zm0 9.5A2.5 2.5 0 1 1 12 6.5a2.5 2.5 0 0 1 0 5z"/></svg></p>
    </div>
  </section>

</main>
</body>
</html>
```